Medical Simulation - Creative Graphic for Data

My company needs a creative graph that depicts the rationales (or reasons) our learners chose certain drug options. Basically, our clients not only want to know how many times certain drugs were selected, but the "whys" behind their choices. I would like a PPT graphic that I can use for other deliverables, where I can simply switch out the drug (treatment) names, the "whys" (what we call rationales), and the specific metrics (percentages, "n" numbers, etc), and the graphic will update and adjust to the new information. The title of the graph (or the slide where the graph will live) should be something like "Treatment Rationales" or something to that effect. Include a placeholder for text to go if anyone wants to add an analysis of the graphic later. This placeholder should accommodate 2-3 bullet points of text. We want this graphic to not just be an image, but organized in a way that you would see in a presentation slide, with a title, place holder for analysis (as indicated above), branding colors, and helpful information to understand the graphic (what is included in this post and it's associated attachments).

I've included specific drug names, rationales, and metrics to use for this (please see excel document). If you are going to design the graph directly in PPT, please use the PPT template design included. Please don't feel like you have to use 1 slide only or can have multiple graphs, if that makes sense for you design idea. They just need to fit within the coloring of the PPT. For font, please use Arial. Below is a Google Drive Link to branding colors and vector art.

https://files.brivoshare.net/open?id=4KQ2TrLm8-XpVd71sNcYhWuPzAe

We are open to many variations and design ideas. Please don't feel like you have to limit yourself! I've attached a few ideas that we've had and it may be a good place to start. We would ESPECIALLY like to see a version utilizing the radial graph (similar to the one included in the Rationales_DesignIdeas document).

Please reach out if you have any questions. Thanks!

Industry/Entity Type

Drug

Requirements
Nice to have
• It would be great to see the radial graph as a design variation (see link below)
• http://6.plotvenna.com/products/plotvenna/docs/users-guide/img/Samples/radar-chart-fixed-radius.png

```html
<!DOCTYPE html>
<html lang="en">
<head>
<meta charset="utf-8">
<title>Treatment Rationales</title>
<link href="https://fonts.googleapis.com/css2?family=Arimo:wght@400;700&display=swap" rel="stylesheet">
<style>
  :root{
    --navy:#0b3d5c;
    --orange:#f7964a;
    --sky:#86c5e8;
    --slate:#555a5e;
    --grid:#e2e2e2;
    --muted:#8c8c8c;
    --body:#7a7a7a;
    --white:#ffffff;
  }
  *{margin:0;padding:0;box-sizing:border-box}
  html,body{width:800px;height:1200px;overflow:hidden;background:var(--white)}
  body{position:relative;font-family:"Arimo",Arial,sans-serif;color:var(--navy)}
  .slide{position:absolute;left:8px;top:306px;width:784px;height:588px;background:var(--white);overflow:hidden}
  .top-band{position:absolute;left:0;top:0;width:784px;height:18px;background:var(--navy)}
  .brand-tab{position:absolute;right:0;top:18px;width:240px;height:20px;
    background:linear-gradient(90deg,rgba(247,150,74,0) 0%,rgba(247,150,74,.55) 35%,var(--orange) 70%);
    color:var(--white);font-weight:700;font-size:13px;letter-spacing:3px;text-align:right;padding-right:16px;line-height:20px}
  .title-bar{position:absolute;left:0;top:18px;width:570px;height:82px;
    background:linear-gradient(180deg,#eeeeee 0%,#ffffff 14%);
    box-shadow:0 4px 5px -3px rgba(0,0,0,.18)}
  .title{position:absolute;left:34px;top:58px;font-size:32px;font-weight:700;letter-spacing:.3px;color:var(--navy);line-height:1}
  .chart{position:absolute;left:88px;top:118px;width:568px;height:376px}
  .chart text{font-family:"Arimo",Arial,sans-serif}
  .n-label{font-size:18px;font-weight:700;fill:var(--navy)}
  .drug{font-size:12px;fill:var(--muted)}
  .pct{font-size:13px;fill:var(--navy);text-anchor:end}
  .legend{position:absolute;left:96px;top:419px;list-style:none;font-size:9px;color:var(--body)}
  .legend li{display:flex;align-items:center;height:16.3px}
  .legend .key{position:relative;width:24px;height:2.5px;margin-right:1px}
  .legend .key::after{content:"";position:absolute;left:8px;top:-2.5px;width:7px;height:7px;border-radius:50%;background:inherit}
  .key.side{background:var(--orange)} .key.life{background:var(--navy)}
  .key.future{background:var(--sky)} .key.guide{background:var(--slate)}
  .analysis{position:absolute;left:517px;top:418px;width:240px;color:var(--body);font-size:10px;line-height:11.8px}
  .analysis h2{font-size:11.5px;font-weight:700;color:var(--navy);margin-bottom:6px}
  .analysis ul{list-style:none;margin-top:1px}
  .analysis li{position:relative;padding-left:15px}
  .analysis li::before{content:"•";position:absolute;left:0;font-size:8px}
  .footnote{position:absolute;left:25px;top:558px;font-size:9.5px;color:var(--navy)}
  .footer{position:absolute;left:0;bottom:0;width:784px;height:18px;background:var(--navy);color:var(--white);font-size:8.5px;text-align:center;line-height:18px}
</style>
</head>
<body>
<section class="slide">
  <div class="top-band"></div>
  <div class="title-bar"></div>
  <div class="brand-tab">EDUCATION</div>
  <h1 class="title">TREATMENT RATIONALES</h1>

  <svg class="chart" viewBox="120 530 710 470" role="img" aria-label="Radar chart of treatment rationales by regimen">
    <g transform="translate(480 740)" fill="none" stroke="var(--grid)" stroke-width="1">
      <g vector-effect="non-scaling-stroke">
        <polygon transform="scale(31)" vector-effect="non-scaling-stroke" points="0,-1 .782,-.623 .975,.223 .434,.901 -.434,.901 -.975,.223 -.782,-.623"/>
        <polygon transform="scale(62)" vector-effect="non-scaling-stroke" points="0,-1 .782,-.623 .975,.223 .434,.901 -.434,.901 -.975,.223 -.782,-.623"/>
        <polygon transform="scale(93)" vector-effect="non-scaling-stroke" points="0,-1 .782,-.623 .975,.223 .434,.901 -.434,.901 -.975,.223 -.782,-.623"/>
        <polygon transform="scale(124)" vector-effect="non-scaling-stroke" points="0,-1 .782,-.623 .975,.223 .434,.901 -.434,.901 -.975,.223 -.782,-.623"/>
        <polygon transform="scale(155)" vector-effect="non-scaling-stroke" points="0,-1 .782,-.623 .975,.223 .434,.901 -.434,.901 -.975,.223 -.782,-.623"/>
      </g>
      <line x1="0" y1="0" x2="121.2" y2="-96.6"/>
      <line x1="0" y1="0" x2="151.1" y2="34.6"/>
      <line x1="0" y1="0" x2="67.3" y2="139.7"/>
      <line x1="0" y1="0" x2="-67.3" y2="139.7"/>
      <line x1="0" y1="0" x2="-151.1" y2="34.6"/>
      <line x1="0" y1="0" x2="-121.2" y2="-96.6"/>
    </g>
    <line x1="480" y1="580" x2="480" y2="866" stroke="#a8a8a8" stroke-width="1"/>

    <g class="pct">
      <text x="464" y="590">50%</text>
      <text x="464" y="621">40%</text>
      <text x="464" y="652">30%</text>
      <text x="464" y="683">20%</text>
      <text x="464" y="714">10%</text>
      <text x="464" y="745">0%</text>
    </g>

    <g fill="none" stroke-width="4" stroke-linejoin="round">
      <polyline stroke="var(--slate)" points="502,786 425,855 331,773 388,666 480,585 545,688"/>
      <polyline stroke="var(--orange)" points="523,705 630,773 546,878 470,768"/>
      <polyline stroke="var(--navy)" points="440,707 480,585 567,670 630,773 503,786 468,763"/>
      <polyline stroke="var(--sky)" points="331,773 416,689"/>
    </g>
    <g fill="var(--slate)">
      <circle cx="480" cy="585" r="5"/><circle cx="545" cy="688" r="5"/>
      <circle cx="425" cy="855" r="5"/><circle cx="331" cy="773" r="5"/>
      <circle cx="388" cy="666" r="5"/><circle cx="502" cy="786" r="5"/>
    </g>
    <g fill="var(--orange)">
      <circle cx="546" cy="878" r="5"/><circle cx="433" cy="703" r="5"/><circle cx="470" cy="768" r="4"/>
    </g>
    <g fill="var(--navy)">
      <circle cx="567" cy="670" r="5"/><circle cx="630" cy="773" r="5"/>
      <circle cx="468" cy="763" r="5"/><circle cx="440" cy="707" r="5"/>
    </g>
    <g fill="var(--sky)">
      <circle cx="523" cy="705" r="5"/><circle cx="416" cy="689" r="5"/>
    </g>

    <g text-anchor="middle">
      <text class="n-label" x="480" y="555">n = 20</text>
      <text class="drug" x="480" y="575">irinotecan</text>

      <text class="n-label" x="687" y="618">n = 100</text>
      <text class="drug" x="694" y="635">irinotecan/leucovorin/5-FU plus</text>
      <text class="drug" x="694" y="650">bevacizumab</text>

      <text class="n-label" x="711" y="753">n = 30</text>
      <text class="drug" x="726" y="771">irinotecan/leucovorin/5-FU plus</text>
      <text class="drug" x="726" y="785">cetuximab</text>

      <text class="n-label" x="620" y="867">n = 70</text>

      <text class="n-label" x="330" y="861">n = 50</text>
      <text class="drug" x="330" y="879">oxaliplatin/capecitabine plus</text>
      <text class="drug" x="330" y="894">bevacizumab</text>

      <text class="n-label" x="251" y="760">n = 30</text>

      <text class="n-label" x="274" y="618">n = 50</text>
      <text class="drug" x="266" y="635">oxaliplatin/leucovorin/5-FU plus</text>
      <text class="drug" x="266" y="650">bevacizumab</text>
    </g>
    <text class="drug" x="550" y="886">oxaliplatin/capecitabine</text>
    <text class="drug" x="323" y="778" text-anchor="end">oxaliplatin/leucovorin/5-FU</text>
  </svg>

  <ul class="legend">
    <li><span class="key side"></span>Fewer overall side effects</li>
    <li><span class="key life"></span>Impact on quality of life</li>
    <li><span class="key future"></span>Preserves future treatment options</li>
    <li><span class="key guide"></span>Recent guidelines</li>
  </ul>

  <div class="analysis">
    <h2>Heading Here</h2>
    <p>Sed do eiusmod tempor incididunt ut labore et dolore magna aliqua. Ut enim ad minim</p>
    <ul>
      <li>Duis aute irure dolor in reprehenderit in voluptate velit esse cillum</li>
      <li>dolore eu fugiat nulla pariatur. Excepteur sint occaecat cupidatat non</li>
      <li>proident, sunt in culpa qui officia deserunt mollit anim id est laborum.</li>
    </ul>
  </div>

  <p class="footnote">*Learners can select 1-2 rationales for each treatment ordered</p>
  <div class="footer">Medivance Learning Confidential and Proprietary Information</div>
</section>
</body>
</html>
```